Keystone Allies Website

My business has been word of mouth over the last 3 years and has grown. Now I need a website for additional marketing as we have new clients asking for a website.

You have already completed my Logo during an earlier project. I have attached the logo.

We do Staff Augmentation and Operation Support.

What is that?
Staff augmentation is an outsourcing strategy that allows companies to fill specific, temporary roles to achieve business objectives. This staffing method complements existing teams with specific talent, enhancing business capabilities or filling gaps left by members on extended leave.

We work alongside the internal recruiting team to assist clients to meet and exceed financial goals.

```html
<!DOCTYPE html>
<html lang="en">
<head>
<meta charset="utf-8">
<title>Keystone Allies</title>
<link href="https://fonts.googleapis.com/css2?family=Montserrat:wght@400;500;600;700&family=Roboto:ital,wght@0,400;1,400&display=swap" rel="stylesheet">
<style>
:root{
  --brand:#0b5078;
  --brand-deep:#094a70;
  --ink:#3d3d3d;
  --grey:#6b6b6b;
  --white:#ffffff;
}
*{margin:0;padding:0;box-sizing:border-box}
html,body{width:1200px;height:3741px;overflow:hidden}
body{position:relative;background:var(--white);font-family:'Roboto',Arial,sans-serif;color:var(--ink)}
.abs{position:absolute}
.head{font-family:'Montserrat',Arial,sans-serif;font-weight:700;color:var(--brand)}

/* header + hero */
.hero{left:0;top:0;width:1200px;height:612px;
  background:
    linear-gradient(90deg,rgba(246,247,249,.97) 0%,rgba(240,243,246,.9) 30%,rgba(240,243,246,.35) 55%,rgba(240,243,246,0) 75%),
    radial-gradient(ellipse 260px 220px at 840px 260px,#3a4a6a 0%,rgba(58,74,106,0) 100%),
    radial-gradient(ellipse 240px 260px at 1060px 420px,#2a2d33 0%,rgba(42,45,51,0) 100%),
    radial-gradient(ellipse 300px 90px at 800px 520px,#f4f4f2 0%,rgba(244,244,242,0) 100%),
    radial-gradient(ellipse 160px 70px at 820px 590px,#b5493f 0%,rgba(181,73,63,0) 100%),
    linear-gradient(160deg,#eef1f0 0%,#dfe6e4 40%,#c8d0cf 70%,#a9b2b4 100%)}
.brand{left:67px;top:26px;display:flex;align-items:center;gap:12px}
.brand-dot{width:50px;height:50px;border-radius:50%;background:var(--brand)}
.brand-name{font-family:'Montserrat',Arial,sans-serif;font-weight:600;color:var(--brand);font-size:26px;line-height:.95}
.brand-name small{display:block;font-size:18px;color:#6a6a6a;font-weight:600}
.nav{top:46px;left:487px;font-family:'Montserrat',Arial,sans-serif;font-weight:500;font-size:18px;color:var(--brand)}
.nav span{position:absolute;white-space:nowrap}
.nav .active::after{content:"";position:absolute;left:2px;right:2px;top:28px;height:4px;border-radius:2px;background:#666}
.welcome{left:86px;top:230px;font-family:'Montserrat',Arial,sans-serif;font-weight:600;font-size:24px;color:#666}
.hero-title{left:81px;top:268px;font-size:64px;line-height:1}
.hero-sub{left:83px;top:328px;font-family:'Montserrat',Arial,sans-serif;font-weight:600;font-size:38px;color:#666;line-height:1}
.btn-solid{left:81px;top:392px;width:143px;height:43px;border-radius:22px;background:var(--brand);color:var(--white);font-family:'Montserrat',Arial,sans-serif;font-weight:700;font-size:15px;display:flex;align-items:center;justify-content:center}

/* section titles */
.sec-title{display:flex;align-items:center;gap:14px;font-size:46px;line-height:1;white-space:nowrap}
.sec-dot{width:44px;height:44px;border-radius:50%;background:var(--brand)}

/* services */
.card-img{width:409px;height:273px}
.card-title{font-size:29px;white-space:nowrap}
.card-text{width:392px;font-size:17px;line-height:22.5px;color:var(--ink)}
.btn-line{height:51px;width:170px;border:2px solid var(--brand);border-radius:26px;color:var(--brand);font-family:'Montserrat',Arial,sans-serif;font-weight:500;font-size:18px;display:flex;align-items:center;justify-content:center}

/* about */
.about{left:0;top:1507px;width:1200px;height:610px;overflow:hidden;
  background:linear-gradient(90deg,#0a4f77 0%,#0b5078 55%,#0a4c72 100%)}
.about-img{left:629px;top:0;width:530px;height:530px;border-radius:50%;
  background:
    radial-gradient(ellipse 120px 140px at 270px 110px,#e9c9b2 0%,rgba(233,201,178,0) 100%),
    radial-gradient(ellipse 150px 220px at 230px 250px,#6b3f2a 0%,rgba(107,63,42,0) 100%),
    radial-gradient(ellipse 190px 220px at 200px 400px,#dedad2 0%,rgba(222,218,210,0) 100%),
    radial-gradient(ellipse 120px 160px at 380px 360px,#bcd6e6 0%,rgba(188,214,230,0) 100%),
    linear-gradient(160deg,#d4c2b2 0%,#9aa8b4 50%,#5c7890 100%)}
.about-ring{left:674px;top:45px;width:440px;height:440px;border-radius:50%;border:42px solid var(--brand);opacity:.92}
.about-title{left:174px;top:93px;color:var(--white)}
.about-title .sec-dot{background:var(--white)}
.about-text{left:174px;top:182px;width:425px;font-size:18px;line-height:27px;color:var(--white)}
.btn-ghost{left:171px;top:476px;width:185px;height:51px;border:2px solid var(--white);border-radius:26px;color:var(--white);font-family:'Montserrat',Arial,sans-serif;font-weight:500;font-size:21px;display:flex;align-items:center;justify-content:center}

/* why */
.feature{width:240px;text-align:center}
.feature-icon{width:158px;height:158px;border-radius:50%;background:var(--brand);margin:0 auto;display:flex;align-items:center;justify-content:center}
.feature-name{margin-top:28px;font-family:'Montserrat',Arial,sans-serif;font-weight:500;font-size:22px;color:var(--brand)}
.feature-text{margin:22px auto 0;width:212px;font-size:16.5px;line-height:22.5px;color:var(--grey)}

/* testimonial */
.testimonial{left:0;top:2812px;width:1200px;height:537px;
  background:
    radial-gradient(ellipse 260px 300px at 120px 250px,#c3c9cf 0%,rgba(195,201,207,0) 100%),
    radial-gradient(ellipse 260px 300px at 1080px 250px,#c6ccd2 0%,rgba(198,204,210,0) 100%),
    linear-gradient(90deg,#dde1e5,#f0f2f4 40%,#f0f2f4 60%,#dde1e5)}
.quote{left:315px;top:2976px;width:570px;text-align:center;font-style:italic;font-size:20.5px;line-height:27px;color:#222}
.avatar{left:524px;top:3087px;width:152px;height:152px;border-radius:50%;border:4px solid var(--brand);
  background:radial-gradient(ellipse 40px 48px at 50% 40%,#c9a48e 0%,rgba(201,164,142,0) 100%),linear-gradient(180deg,#ece9e5 0%,#f7f6f4 60%,#d8d4cf 100%)}
.client{left:500px;top:3266px;width:200px;text-align:center;font-family:'Montserrat',Arial,sans-serif;font-weight:600;font-size:22px;color:var(--brand)}

/* footer */
.footer{left:0;top:3349px;width:1200px;height:392px;background:linear-gradient(90deg,#0a4a70,#0b5078 50%,#0a4a70)}
.foot-brand{left:447px;top:3420px;display:flex;align-items:center;gap:14px}
.foot-brand .brand-dot{width:80px;height:80px;background:var(--white)}
.foot-brand .brand-name{color:var(--white);font-size:36px;line-height:.9}
.foot-brand .brand-name small{color:var(--white);font-size:25px}
.foot-nav{left:0;top:3558px;width:1200px;display:flex;justify-content:center;gap:24px;font-family:'Montserrat',Arial,sans-serif;font-size:19px;color:var(--white)}
.copy{left:0;top:3613px;width:1200px;text-align:center;font-size:17px;color:var(--white)}
.social{top:3674px;width:34px;height:34px;border-radius:50%;background:var(--white)}
</style>
</head>
<body>

<div class="abs hero" role="img" aria-label="Photo of a business meeting: a presenter standing beside a table with colleagues in a bright office"></div>
<div class="abs brand"><div class="brand-dot"></div><div class="brand-name">KEYSTONE<small>ALLIES,LLC</small></div></div>
<nav class="abs nav">
  <span class="active" style="left:0">HOME</span>
  <span style="left:84px">SERVICES</span>
  <span style="left:196px">ABOUT US</span>
  <span style="left:318px">TESTIMONIALS</span>
  <span style="left:482px">CONTACT US</span>
</nav>
<div class="abs welcome">WELCOME TO</div>
<div class="abs head hero-title">KEYSTONE</div>
<div class="abs hero-sub">ALLIES,LLC</div>
<div class="abs btn-solid">READ MORE</div>

<div class="abs head sec-title" style="left:388px;top:722px"><span class="sec-dot"></span>WHAT WE DO?</div>

<div class="abs card-img" style="left:173px;top:828px;background:radial-gradient(ellipse 220px 90px at 50% 22%,#d6c3b4 0%,rgba(214,195,180,0) 100%),linear-gradient(180deg,#b69e8c 0%,#8d8880 30%,#3c4a63 60%,#6e7d92 85%,#9c8f82 100%)" role="img" aria-label="Photo of a smiling group of colleagues standing together"></div>
<div class="abs head card-title" style="left:174px;top:1128px">STAFF AUGMENTATION</div>
<p class="abs card-text" style="left:174px;top:1182px">Lorem ipsum dolor sit amet, consectetur adipiscin elit, sed do eiusmod tempor incididunt ut labor et dolore magna aliqua. Ut enim ad minim veniam, quis nostrud exercitation ullamco laboris</p>
<div class="abs btn-line" style="left:173px;top:1299px">READ MORE</div>

<div class="abs card-img" style="left:617px;top:828px;background:radial-gradient(ellipse 160px 110px at 45% 50%,#d9a88f 0%,rgba(217,168,143,0) 100%),linear-gradient(135deg,#faefe9 0%,#f0d9cc 40%,#b8a8a0 70%,#2f3944 100%)" role="img" aria-label="Photo of two hands holding each other in support"></div>
<div class="abs head card-title" style="left:618px;top:1128px">OPERATION SUPPORT</div>
<p class="abs card-text" style="left:618px;top:1182px">Lorem ipsum dolor sit amet, consectetur adipiscin elit, sed do eiusmod tempor incididunt ut labor et dolore magna aliqua. Ut enim ad minim veniam, quis nostrud exercitation ullamco labori</p>
<div class="abs btn-line" style="left:617px;top:1299px">READ MORE</div>

<section class="abs about">
  <div class="abs about-img" role="img" aria-label="Photo of a smiling businesswoman in a light blazer"></div>
  <div class="abs about-ring"></div>
  <div class="abs head sec-title about-title"><span class="sec-dot"></span>ABOUT US</div>
  <p class="abs about-text">Lorem ipsum dolor sit amet, consectetur adipiscing elit, sed do eiusmod tempor incididunt ut labore et dolore magna aliqua. Ut enim ad minim veniam, quis nostrud exercitation ullamco laboris nisi ut aliquip ex ea commodo consequat. Duis aute irure dolor in reprehenderit in voluptate velit esse cillum dolore eu fugiat nulla pariatur. Excepteur sint occaecat cupidatat non proident, sunt in culpa qui officia deserunt mollit anim id est labo</p>
  <div class="abs btn-ghost">READ MORE</div>
</section>

<div class="abs head sec-title" style="left:330px;top:2221px"><span class="sec-dot"></span>WHY CHOOSE US?</div>

<div class="abs feature" style="left:97px;top:2326px">
  <div class="feature-icon"><svg width="96" height="96" viewBox="0 0 96 96" fill="none" stroke="#fff" stroke-width="6"><circle cx="48" cy="26" r="14"/><path d="M24 62c4-14 44-14 48 0"/><g fill="#fff" stroke="none"><path d="M22 70l3 7h7l-6 4 2 7-6-4-6 4 2-7-6-4h7z"/><path d="M48 70l3 7h7l-6 4 2 7-6-4-6 4 2-7-6-4h7z"/><path d="M74 70l3 7h7l-6 4 2 7-6-4-6 4 2-7-6-4h7z"/></g></svg></div>
  <div class="feature-name">Finibus Bonoru</div>
  <p class="feature-text">Lorem ipsum dolor sit et, consectetur adipi scinelited do eiusmod temporincidint ut lab or et dolore ma</p>
</div>
<div class="abs feature" style="left:348px;top:2326px">
  <div class="feature-icon"><svg width="100" height="90" viewBox="0 0 100 90" fill="none" stroke="#fff" stroke-width="5"><rect x="6" y="10" width="66" height="44" rx="3"/><path d="M30 66h22M41 54v12"/><rect x="64" y="34" width="26" height="44" rx="4" fill="#0b5078"/><circle cx="40" cy="32" r="12"/><path d="M40 20v12h12"/></svg></div>
  <div class="feature-name">Finibus Bonoru</div>
  <p class="feature-text">Lorem ipsum dolor sit et, consectetur adipi scinelited do eiusmod temporincidint ut lab or et dolore ma</p>
</div>
<div class="abs feature" style="left:601px;top:2326px">
  <div class="feature-icon"><svg width="90" height="100" viewBox="0 0 90 100" fill="none" stroke="#fff" stroke-width="5"><circle cx="45" cy="38" r="28"/><circle cx="45" cy="38" r="18"/><path d="M45 28l3 7h7l-6 4 2 7-6-4-6 4 2-7-6-4h7z" fill="#fff" stroke="none"/><path d="M28 62l-8 30 12-6 6 10 7-26M62 62l8 30-12-6-6 10-7-26"/></svg></div>
  <div class="feature-name">Finibus Bonoru</div>
  <p class="feature-text">Lorem ipsum dolor sit et, consectetur adipi scinelited do eiusmod temporincidint ut lab or et dolore ma</p>
</div>
<div class="abs feature" style="left:853px;top:2326px">
  <div class="feature-icon"><svg width="84" height="84" viewBox="0 0 84 84" fill="#fff"><path d="M4 4h28l-9 9 12 12-10 10-12-12-9 9zM80 4v28l-9-9-12 12-10-10 12-12-9-9zM4 80V52l9 9 12-12 10 10-12 12 9 9zM80 80H52l9-9-12-12 10-10 12 12 9-9z"/></svg></div>
  <div class="feature-name">Finibus Bonoru</div>
  <p class="feature-text">Lorem ipsum dolor sit et, consectetur adipi scinelited do eiusmod temporincidint ut lab or et dolore ma</p>
</div>

<div class="abs testimonial" role="img" aria-label="Faded photo of colleagues talking in an office"></div>
<div class="abs head" style="left:0;top:2886px;width:1200px;text-align:center;font-size:46px">TESTIMONIAL</div>
<p class="abs quote">Lorem ipsum dolor sit amet, consectetur adipiscing elit, sed do eiusmod tempor incididunt ut labore et dolore magna aliqua uis ipsum suspendisse ultrices gravida.</p>
<svg class="abs" style="left:76px;top:3034px" width="28" height="50" viewBox="0 0 28 50" fill="none" stroke="#555" stroke-width="3"><path d="M26 2L3 25l23 23"/></svg>
<svg class="abs" style="left:1098px;top:3034px" width="28" height="50" viewBox="0 0 28 50" fill="none" stroke="#555" stroke-width="3"><path d="M2 2l23 23L2 48"/></svg>
<div class="abs avatar" role="img" aria-label="Portrait photo of a client"></div>
<div class="abs client">MARLEE</div>

<div class="abs footer"></div>
<div class="abs foot-brand"><div class="brand-dot"></div><div class="brand-name">KEYSTONE<small>ALLIES,LLC</small></div></div>
<div class="abs foot-nav"><span>HOME</span><span>ABOUT US</span><span>SERVICES</span><span>TESTIMONIALS</span><span>CONTACT US</span></div>
<div class="abs copy">Copyright 2022 &nbsp;All Rights Reserved &nbsp; Terms &amp; Conditions</div>
<div class="abs social" style="left:536px"></div>
<div class="abs social" style="left:583px"></div>
<div class="abs social" style="left:630px"></div>

</body>
</html>
```